VEXA New York *Luxury Candles*

We need a logo AND package design for a new private label luxury candle company.
I'm an interior decorator. When you enter a space you can perceive design as a 3 dimensional experience. However, the perfect scent in a space makes your experience unforgettable and 4 dimensional. Scents have the power to evoke pleasure and bring back memories.
I want my costumer to have a luxurious experience from the moment they see the package, open it, smell, enjoy and use it to decorate their spaces.
We are looking for a clean design that reads LUX. I'm attaching some pictures for Inspiration.
The candle is approximately 4 inches high 3.5 inches wide (10.3cm high, 9cm wide).

The company's name is

VEXA
New York

Target Market(s)

Women between 27 and 50 who like design, elegance, and beautiful spaces.
They like to indulge and create their safety sanctuary at home.

Industry/Entity Type

It Company

Font styles to use
Sans Serif
Script

Requirements
Must have
• A design for the candle and a design for the gift box + logo
Nice to have
• Simplicity
• Elegance
• Efortless beauty
Should not have
• Many different colors
• Shouldn't be overdone

```html
<!DOCTYPE html>
<html lang="en">
<head>
<meta charset="utf-8">
<title>VEXA New York – Gift Box and Candle Label</title>
<link href="https://fonts.googleapis.com/css2?family=Montserrat:wght@300;400;500&display=swap" rel="stylesheet">
<style>
  :root {
    --teal: #14a4c9;
    --teal-soft: #8fd3e6;
    --gold: #bf9f55;
    --ink: #3a3a3a;
    --stage-grey: #d7d7d7;
    --paper: #ffffff;
    --frost: #f3f3f1;
  }
  html, body {
    margin: 0;
    padding: 0;
    width: 1200px;
    height: 1200px;
    overflow: hidden;
    font-family: "Montserrat", Arial, sans-serif;
  }
  .canvas {
    position: relative;
    width: 1200px;
    height: 1200px;
    background: var(--paper);
  }

  /* ---------- Gift box front panel ---------- */
  .box-section {
    position: absolute;
    left: 0; top: 0;
    width: 1200px;
    height: 724px;
    background: var(--stage-grey);
  }
  .box-face {
    position: absolute;
    left: 370px; top: 110px;
    width: 460px; height: 460px;
    background: var(--paper);
    overflow: hidden;
  }
  .floral-band {
    position: absolute;
    left: 0; top: 0;
    width: 460px; height: 200px;
    background: linear-gradient(200deg, var(--teal-soft) 0%, rgba(143,211,230,0.45) 45%, rgba(255,255,255,0) 100%);
  }
  .box-title {
    position: absolute;
    left: 0; top: 235px;
    width: 460px;
    text-align: center;
    font-weight: 300;
    font-size: 17px;
    letter-spacing: 0.5px;
    color: var(--ink);
    margin: 0;
  }
  .box-subtitle {
    position: absolute;
    left: 0; top: 266px;
    width: 460px;
    text-align: center;
    font-weight: 300;
    font-size: 14px;
    color: var(--ink);
    margin: 0;
  }
  .box-band {
    position: absolute;
    left: 0; bottom: 0;
    width: 460px; height: 140px;
    background: var(--teal);
  }

  /* ---------- Brand lockup ---------- */
  .brand {
    position: absolute;
    display: flex;
    flex-direction: column;
    align-items: center;
  }
  .brand-name {
    display: flex;
    align-items: center;
    gap: 10px;
    font-weight: 400;
    letter-spacing: 6px;
    margin: 0;
  }
  .brand-square {
    display: inline-block;
  }
  .brand-city {
    margin: 0;
    font-weight: 500;
    letter-spacing: 4px;
    color: var(--gold);
  }
  .box-face .brand {
    left: 0; bottom: 26px; width: 460px;
  }
  .box-face .brand-name {
    font-size: 40px;
    color: var(--paper);
  }
  .box-face .brand-square {
    width: 22px; height: 22px;
    background: var(--paper);
  }
  .box-face .brand-city {
    font-size: 13px;
    margin-top: 14px;
  }

  /* ---------- Candle vessel label ---------- */
  .candle-section {
    position: absolute;
    left: 0; top: 724px;
    width: 1200px; height: 476px;
    background: var(--paper);
  }
  .vessel {
    position: absolute;
    left: 463px; top: 52px;
    width: 274px; height: 384px;
    background: linear-gradient(90deg, #e9e9e6 0%, var(--frost) 18%, #fbfbfa 55%, #ecece9 100%);
    clip-path: polygon(0 0, 100% 0, 96% 100%, 4% 100%);
    border-radius: 14px;
  }
  .vessel-rim {
    position: absolute;
    left: 463px; top: 52px;
    width: 274px; height: 26px;
    border-radius: 137px / 13px;
    border: 1px solid #dcdcd8;
    box-sizing: border-box;
    background: #f7f7f5;
  }
  .vessel .brand {
    left: 0; top: 100px; width: 274px;
  }
  .vessel .brand-name {
    font-size: 36px;
    color: var(--teal);
  }
  .vessel .brand-square {
    width: 20px; height: 20px;
    background: var(--teal);
  }
  .vessel .brand-city {
    font-size: 12px;
    margin-top: 14px;
  }
  .vessel-scent {
    position: absolute;
    left: 0; top: 228px;
    width: 274px;
    text-align: center;
    font-weight: 300;
    font-size: 12.5px;
    color: var(--gold);
    margin: 0;
  }
  .vessel-details {
    position: absolute;
    left: 0; top: 318px;
    width: 274px;
    text-align: center;
    font-weight: 300;
    color: var(--gold);
    margin: 0;
  }
  .vessel-weight { font-size: 10.5px; display: block; }
  .vessel-wax { font-size: 12px; display: block; margin-top: 8px; }
</style>
</head>
<body>
<main class="canvas">

  <section class="box-section" aria-label="Gift box front panel">
    <div class="box-face">
      <div class="floral-band" role="img" aria-label="Blue line-drawn anemone flowers cascading across the top corner"></div>
      <p class="box-title">CASHMERE SIGNATURE SCENT</p>
      <p class="box-subtitle">100% Soy Wax</p>
      <div class="box-band"></div>
      <div class="brand">
        <p class="brand-name"><span class="brand-square"></span>VEXA</p>
        <p class="brand-city">NEW YORK</p>
      </div>
    </div>
  </section>

  <section class="candle-section" aria-label="Candle vessel label">
    <div class="vessel">
      <div class="brand">
        <p class="brand-name"><span class="brand-square"></span>VEXA</p>
        <p class="brand-city">NEW YORK</p>
      </div>
      <p class="vessel-scent">CASHMERE SIGNATURE SCENT</p>
      <p class="vessel-details">
        <span class="vessel-weight">9 Oz / 255 g</span>
        <span class="vessel-wax">100% Soy Wax</span>
      </p>
    </div>
    <div class="vessel-rim"></div>
  </section>

</main>
</body>
</html>
```